Business Card Design Project for an English Teacher

I need a business card design for my new job.
I'd like to start teaching English as a freelance.
My students will be children, teenager, and adults, who don't like or hesitate to study English and I would like to open a door to the new world for them.

I'd like to put the information below;
[right side]
1. name
2. mail address
3. mobile number
4. website or facebook page

[back]
1.my message: Feel free at asking me anything about my classes

2.lesson list such as:
price: 3150 yen ~

calsses:
kids class( mum& dad can join) ... 30 minutes / 45 minutes
students (over age 13).... 60minutes / 90 minutes
Adult (over age 19) .... 60 minutes / 90 minutes

3. I'll have both Web Lesson and Face to Face Lesson

4. Free trial lesson

Target Market(s)

My students will be children, teenager, and adults, who don't like or hesitate to study English

Industry/Entity Type

Business

Requirements
Must have
• designed both side

```html
<!DOCTYPE html>
<html lang="en">
<head>
<meta charset="utf-8">
<title>Mika Sorano – English Teaching business card</title>
<link href="https://fonts.googleapis.com/css2?family=Source+Sans+3:wght@300;400;600&display=swap" rel="stylesheet">
<style>
  :root {
    --canvas: #ecebe8;
    --card-light: #fbfbfb;
    --card-shade: #d9d9db;
    --ink: #2b2b2d;
    --ink-soft: #4a4a4c;
    --grey-tag: #7d7d80;
    --navy: #1f3a6e;
    --blue: #0f6fae;
    --sky: #1b87bf;
    --orange: #ff4a0a;
  }
  * { margin: 0; padding: 0; box-sizing: border-box; }
  html, body {
    width: 1200px; height: 800px; overflow: hidden;
    background: var(--canvas);
    font-family: "Source Sans 3", "Myriad Pro", Arial, sans-serif;
    color: var(--ink);
  }
  .stage { position: relative; width: 1200px; height: 800px; }

  .card {
    position: absolute;
    width: 720px; height: 420px;
    background: radial-gradient(ellipse at 55% 45%, var(--card-light) 0%, #efeff0 45%, var(--card-shade) 100%);
    box-shadow: 0 6px 18px rgba(0,0,0,.18);
    overflow: hidden;
  }
  .card__shapes { position: absolute; inset: 0; width: 100%; height: 100%; }

  /* ---------- back side ---------- */
  .card--back { left: 30px; top: 30px; }
  .back__message {
    position: absolute; left: 42px; top: 40px;
    font-size: 16px; font-weight: 600; color: var(--ink);
  }
  .back__list {
    list-style: none; position: absolute; left: 42px;
    font-size: 15px; line-height: 24px; color: var(--ink-soft);
  }
  .back__list li::before { content: "• "; }
  .back__list--classes { top: 64px; }
  .back__heading {
    position: absolute; left: 42px; top: 234px;
    font-size: 16px; font-weight: 600; color: var(--ink);
  }
  .back__list--specialties { top: 258px; }
  .back__brand { position: absolute; left: 420px; top: 318px; }

  /* ---------- front side ---------- */
  .card--front { left: 450px; top: 340px; }
  .front__person { position: absolute; left: 138px; top: 98px; }
  .front__name { font-size: 17px; font-weight: 400; color: var(--ink); }
  .front__role { font-size: 10px; color: var(--sky); margin-left: 30px; margin-top: 2px; }
  .front__contact {
    list-style: none; position: absolute; left: 108px; top: 186px;
    font-size: 11.5px; line-height: 19px; color: var(--ink);
  }
  .front__brand { position: absolute; right: 40px; top: 58px; text-align: right; }

  /* ---------- brand wordmark ---------- */
  .brand__name {
    font-size: 40px; font-weight: 300; letter-spacing: 1px;
    color: var(--sky); line-height: 1;
  }
  .brand__tagline {
    font-size: 15px; font-weight: 400; letter-spacing: 6px;
    color: var(--grey-tag); margin-top: 4px;
  }
  .card--back .brand__name { font-size: 50px; opacity: .85; }
  .card--back .brand__tagline { font-size: 22px; letter-spacing: 8px; }
</style>
</head>
<body>
<main class="stage">

  <section class="card card--back" aria-label="Back of business card">
    <svg class="card__shapes" viewBox="0 0 720 420" aria-hidden="true">
      <polygon points="672,0 720,0 720,52" fill="var(--navy)"/>
      <polygon points="0,290 0,420 128,420" fill="var(--blue)"/>
    </svg>
    <p class="back__message">Feel free at asking me anything about my classes</p>
    <ul class="back__list back__list--classes">
      <li>Kids class( mum&amp; dad can join) ... 30 minutes / 45 minutes</li>
      <li>Students (over age 13).... 60minutes / 90 minutes</li>
      <li>Adult (over age 19) .... 60 minutes / 90 minutes</li>
    </ul>
    <p class="back__heading">Specialties:</p>
    <ul class="back__list back__list--specialties">
      <li>I'll have both Web Lesson and Face to Face Lesson</li>
      <li>Free trial lesson</li>
      <li>Lesson list such as: price: 3150 yen ~</li>
    </ul>
    <div class="back__brand">
      <p class="brand__name">Mika Sorano</p>
      <p class="brand__tagline">ENGLISH TEACHING</p>
    </div>
  </section>

  <section class="card card--front" aria-label="Front of business card">
    <svg class="card__shapes" viewBox="0 0 720 420" aria-hidden="true">
      <polygon points="0,372 0,420 26,420" fill="var(--sky)"/>
      <polygon points="84,0 136,0 136,44 66,420 14,420 14,378" fill="var(--orange)"/>
      <polygon points="676,0 720,0 720,48" fill="var(--sky)"/>
    </svg>
    <div class="front__person">
      <p class="front__name">Mika Sorano</p>
      <p class="front__role">Teacher</p>
    </div>
    <ul class="front__contact">
      <li>Cras sollicitudin scelerisque venenatis</li>
      <li>+123 456 789</li>
      <li>mikasorano@mailbox.com</li>
      <li>www.mikasorano.com</li>
    </ul>
    <div class="front__brand">
      <p class="brand__name">Mika Sorano</p>
      <p class="brand__tagline">ENGLISH TEACHING</p>
    </div>
  </section>

</main>
</body>
</html>
```